Trade Show Package: Logo, B. Card, Brochure, T Shirt & Signs

We have a trade show coming up and will need the following designed: tri-fold, logo cleanup, business cards, t-shirt text and 6 poster signs.

We want all our materials to be consistent, modern (san serif fonts) contemporary and clean. You can take a look at our website, www.bright-lane-webworks.com to see the color scheme we are using and overall look (we use dark red, grey, black, charcoal grey).

1- Logo Cleanup
Our logo is attached. It needs to be cleaned up and sharp so that it looks really good on all of our materials.
We need a thin red line added to the bottom of the logo. See the logo on the tri-fold on the bottom right.
Perhaps the tagline, business on skyforge88 should be a lighter charcoal grey.

If you have any ideas that you think would make it better, of course we welcome that.

We need the logo cleaned up first as the logo is needed for the business cards, tri-fold, t-shirts and signs.

2- Business Cards
Our business cards will be printed on white paper.
Top has a dark red border, followed by our logo (with thin red line underneath) followed by text.

Here is a screencast of what we are going for: http://clipvault-demo.net/t/QxR7p2kWdnLa
We'll need the two separate cards shown in the screencast.

BASIC STYLE: clean, modern design

FONT: modern, easy to read

COLORS: dark red for the bar at the top (full bleed) and Marcus's name & possibly charcoal grey for the rest of the text

3- Tri-fold
3 (5x7 panels) brochure

This brochure is all about cloud computing. I have attached a plain pdf that I put together just to show the order of the tri-fold; this is not the design we
want, we want a modern design, clean, consistent colors and look.

We have 2 pictures we found but if you think another picture would work better for the design, please
show us your ideas.

Here is what we are looking for:

COLOR: will be printed on white paper, except one page will be black (testimonials page, full bleed);
also we need to have a spot uv on the front and back covers and we want a font that does well with that. The video with the black brochure will show the spot uv we are looking for.

BASIC STYLE: clean, modern and innovative

FONT: modern, easy to read and shows up well on paper (san serif fonts)

Left inside trifold: man in a brown box working - see link I provided at the bottom of that page; let me know the size you require and I'll purchase it and email it to you. We want this page to match or complement the coloring of the rest of our brochure, maybe something like this (reddish overtones? instead of the brown which doesn't go). Picture full bleed.

Middle inside: man lying on grass, dreaming of bubble - see link I provided at the bottom of that page; let me know the size you require and I'll purchase it and email it to you. Picture full bleed.

Right inside: text (boost business with cloud computing) with our logo on the bottom right (the word "might" needs to be in italics)

Outside left: the testimonials goes here, make background black (this page only) with white or other light text, full black bleed

Outside middle: BACK COVER - our logo and address

Outside right: FRONT COVER - text (get your cloud on) and our logo on bottom right (with the thin red line underneath)

4- Shirts
T-SHIRT FRONT: our logo on left side

T-SHIRT BACK:
Ask Me (should be biggest font size and in red)
about (should be on second line and smaller in black)
Cloud Computing (should be on the third line, black text and smaller than ask me but big)

- find a graphical element from our logo and use it here, for example the red line, to make it easier to read and make it interesting
- should be modern (consistent with the rest of our materials, i.e. brochure ...)
- attached a sample look we put together but we need a designed modern look

5- Signs
Here is a preliminary look at our signs (pdf attached), last 2 slides will be updated slightly and sent back to you with dimensions for all the signs.

Text should be 1 1/2 inches from the frames border. Will be printed on a white background.

BASIC STYLE: clean, modern design (something that will draw people to look at the sign)
the thick red rectangle on the bottom with the logo on the right should be more interesting, maybe add gradient, texture, etc.

FONT: modern, easy to read (san serif fonts) first 4 posters should be the same exact font and size.

COLORS: dark red, black, greys, charcoal grey

NOTE: We will only guarantee payment once we see designs that match our criteria. We cannot guarantee until we have SEEN your work.

```html
<!DOCTYPE html>
<html lang="en">
<head>
<meta charset="utf-8">
<title>Get it here – Bright Lane Webworks sign</title>
<link rel="stylesheet" href="https://fonts.googleapis.com/css2?family=Krona+One&display=swap">
<style>
  :root {
    --paper: #ffffff;
    --brand-red: #c4070f;
    --brand-red-deep: #a8050b;
    --brand-red-bright: #d8141c;
    --mist-grey: #d6d6d6;
    --tag-grey: #e6e6e6;
    --type-white: #ffffff;
  }
  html, body {
    margin: 0;
    padding: 0;
    width: 1200px;
    height: 900px;
    overflow: hidden;
    background: var(--paper);
  }
  .sign {
    position: relative;
    width: 1200px;
    height: 900px;
    background: var(--paper);
    font-family: "Krona One", sans-serif;
    overflow: hidden;
  }
  .name-pattern {
    position: absolute;
    inset: 0;
  }
  .name-pattern__item {
    position: absolute;
    top: 372px;
    width: 520px;
    margin-left: -260px;
    margin-top: -40px;
    transform: rotate(55deg);
    color: var(--mist-grey);
    font-size: 40px;
    line-height: 1.15;
    text-align: center;
    white-space: nowrap;
  }
  .name-pattern__item span {
    display: block;
    font-size: 17px;
    margin-top: 10px;
  }
  .headline {
    position: absolute;
    left: 0;
    right: 0;
    top: 292px;
    margin: 0;
    text-align: center;
    padding-left: 20px;
    color: var(--brand-red);
    font-size: 70px;
    font-weight: 400;
    letter-spacing: 2px;
    line-height: 1;
    text-shadow: 3px 4px 3px rgba(0, 0, 0, 0.35);
  }
  .brand-bar {
    position: absolute;
    left: 57px;
    top: 627px;
    width: 1066px;
    height: 89px;
    background: linear-gradient(90deg, var(--brand-red-deep) 0%, var(--brand-red-bright) 55%, var(--brand-red-deep) 100%);
    box-shadow: 0 2px 3px rgba(0, 0, 0, 0.35);
    overflow: hidden;
  }
  .brand-bar__texture {
    position: absolute;
    inset: 0;
    width: 100%;
    height: 100%;
  }
  .brand-bar__name {
    position: absolute;
    right: 30px;
    top: 22px;
    margin: 0;
    color: var(--type-white);
    font-size: 22px;
    font-weight: 400;
    line-height: 1;
    text-align: right;
  }
  .brand-bar__tagline {
    position: absolute;
    right: 36px;
    top: 58px;
    margin: 0;
    color: var(--tag-grey);
    font-size: 10px;
    line-height: 1;
  }
</style>
</head>
<body>
  <main class="sign">
    <div class="name-pattern" aria-hidden="true">
      <div class="name-pattern__item" style="left:250px">Bright Lane<br>Webworks<span>business on skyforge88</span></div>
      <div class="name-pattern__item" style="left:520px">Bright Lane<br>Webworks<span>business on skyforge88</span></div>
      <div class="name-pattern__item" style="left:790px">Bright Lane<br>Webworks<span>business on skyforge88</span></div>
    </div>

    <h1 class="headline">get it here.</h1>

    <div class="brand-bar">
      <svg class="brand-bar__texture" viewBox="0 0 1066 89" preserveAspectRatio="none" aria-hidden="true">
        <defs>
          <pattern id="grain" width="6" height="6" patternUnits="userSpaceOnUse">
            <rect width="6" height="6" fill="none"/>
            <rect x="1" y="2" width="1" height="1" fill="#000" opacity="0.18"/>
            <rect x="4" y="0" width="1" height="1" fill="#fff" opacity="0.10"/>
            <rect x="3" y="4" width="1" height="1" fill="#000" opacity="0.14"/>
            <rect x="0" y="5" width="1" height="1" fill="#fff" opacity="0.08"/>
          </pattern>
          <linearGradient id="sheen" x1="0" y1="0" x2="0" y2="1">
            <stop offset="0" stop-color="#fff" stop-opacity="0.10"/>
            <stop offset="1" stop-color="#000" stop-opacity="0.18"/>
          </linearGradient>
        </defs>
        <rect width="1066" height="89" fill="url(#grain)"/>
        <rect width="1066" height="89" fill="url(#sheen)"/>
      </svg>
      <p class="brand-bar__name">Bright Lane Webworks</p>
      <p class="brand-bar__tagline">business on skyforge88</p>
    </div>
  </main>
</body>
</html>
```